Law Firm in Texas in need of new letterhead

Law Firm in Fort Worth, TX, USA named "Vale & Brennick, Attorneys-At-Law, LLP." This is a general practice law firm that mostly does Family Law and Criminal Defense work.

We are looking for a new letterhead that has a "classical" appeal, with modern elements.

Any color combination is fine, but please note that we do fax many documents, so the design must be clearly legible in Black and White.

We would like our letterhead to project a sense of professionalism, integrity, and ability.

Target Market(s)

Letterhead will be for correspondence generally with other attorneys and clients.

Industry/Entity Type

Law Firm

Logo Text

Vale & Brennick, Attorneys-At-Law, LLP.

Logo styles of interest
Pictorial/Combination Logo
Wordmark Logo
Lettermark Logo
Requirements
Nice to have
• Although not necessary, a "Texas Star" that is incorporated into the design would be a nice touch.
Should not have
• Colors that do not convert to B&W easily

```html
<!DOCTYPE html>
<html lang="en">
<head>
<meta charset="utf-8">
<title>Vale &amp; Brennick Letterhead</title>
<link href="https://fonts.googleapis.com/css2?family=Open+Sans:wght@400;600;700&display=swap" rel="stylesheet">
<style>
  :root{
    --ink:#231f20;
    --paper:#ffffff;
    --backdrop:#e9e9e9;
    --rule-grey:#8a8a8a;
    --rule-light:#c4c4c4;
    --watermark:#e6e6e6;
    --text:#2b2b2b;
  }
  html,body{margin:0;padding:0;overflow:hidden}
  body{width:1200px;height:1000px;background:var(--backdrop);position:relative;
       font-family:"Open Sans",Arial,sans-serif;color:var(--text)}
  .sheet{position:absolute;width:556px;height:792px;background:var(--paper);overflow:hidden;
         box-shadow:0 2px 6px rgba(0,0,0,.18)}
  .sheet--blank{left:36px;top:103px}
  .sheet--letter{left:606px;top:103px}
  .decor{position:absolute;left:0;top:0;width:556px;height:792px}
  .firm-name{position:absolute;left:12px;top:19px;margin:0;font-size:14.5px;font-weight:700;color:var(--ink);letter-spacing:-.1px}
  .address{position:absolute;left:319px;top:21px;font-size:10px;line-height:14px;color:var(--ink)}
  .contacts{position:absolute;left:454px;top:21px;font-size:10px;line-height:14px;color:var(--ink)}
  .contacts div{display:flex;align-items:center;gap:4px}
  .contacts svg{width:9px;height:9px}
  .partners{position:absolute;left:0;bottom:8px;font-size:8px;line-height:10.5px;color:#fff}
  .partners strong{font-weight:700}
  .letter-body{position:absolute;left:40px;top:145px;width:478px;font-size:9.6px;line-height:13.4px;color:var(--text)}
  .letter-body p{margin:0}
  .letter-body .gap{margin-top:13.4px}
  .signature{margin-top:13.4px;padding-left:2px}
</style>
</head>
<body>

<!-- Blank letterhead -->
<section class="sheet sheet--blank">
  <svg class="decor" viewBox="0 0 556 792" aria-hidden="true">
    <circle role="img" aria-label="Faint Texas star emblem watermark" cx="436" cy="587" r="150" fill="var(--watermark)"/>
    <path d="M0,74 C160,50 330,92 556,64" fill="none" stroke="var(--rule-light)" stroke-width="1.5"/>
    <path d="M0,70 C160,46 330,88 556,60" fill="none" stroke="var(--rule-grey)" stroke-width="1.5"/>
    <path d="M0,78 C170,40 330,92 556,76 L556,82 C330,96 170,48 0,84 Z" fill="var(--ink)"/>
    <path d="M0,716 C170,694 360,744 556,718" fill="none" stroke="var(--rule-light)" stroke-width="2"/>
    <path d="M0,720 C170,700 360,750 556,724" fill="none" stroke="var(--rule-grey)" stroke-width="3"/>
    <path d="M0,726 C170,708 360,756 556,730 L556,792 L0,792 Z" fill="var(--ink)"/>
  </svg>
  <h1 class="firm-name">Vale &amp; Brennick, Attorneys-at-Law, LLP</h1>
  <div class="address">2140 E. Marlowe St.<br>Fort Worth, TX 76111</div>
  <div class="contacts">
    <div><svg viewBox="0 0 10 10"><path d="M2 0.5 L3.6 2.4 L2.8 3.6 C3.4 5 4.8 6.4 6.4 7.2 L7.6 6.4 L9.5 8 L8.4 9.6 C4.6 9.4 0.6 5.4 0.4 1.6 Z" fill="var(--ink)"/></svg>(817) 555-0142</div>
    <div><svg viewBox="0 0 10 10"><rect x="2.5" y="0.5" width="5" height="3" fill="var(--ink)"/><rect x="0.5" y="3.5" width="9" height="4" rx="1" fill="var(--ink)"/><rect x="2.5" y="6.5" width="5" height="3" fill="var(--ink)"/></svg>(817) 555-0187</div>
  </div>
  <div class="partners">Partners:<br><strong>Adrian Vale</strong>, Managing Partner (Licensed in State of Texas, United States District Court (Northern District of Texas), United States Supreme Court)<br><strong>Claire Marie Brennick</strong> (Licensed in the State of Texas)</div>
</section>

<!-- Letter sample -->
<section class="sheet sheet--letter">
  <svg class="decor" viewBox="0 0 556 792" aria-hidden="true">
    <circle role="img" aria-label="Faint Texas star emblem watermark" cx="446" cy="587" r="150" fill="var(--watermark)"/>
    <path d="M0,74 C160,50 330,92 556,64" fill="none" stroke="var(--rule-light)" stroke-width="1.5"/>
    <path d="M0,70 C160,46 330,88 556,60" fill="none" stroke="var(--rule-grey)" stroke-width="1.5"/>
    <path d="M0,78 C170,40 330,92 556,76 L556,82 C330,96 170,48 0,84 Z" fill="var(--ink)"/>
    <path d="M0,712 C170,690 360,740 556,714" fill="none" stroke="var(--rule-light)" stroke-width="2"/>
    <path d="M0,716 C170,696 360,746 556,720" fill="none" stroke="var(--rule-grey)" stroke-width="3"/>
    <path d="M0,722 C170,704 360,752 556,726 L556,792 L0,792 Z" fill="var(--ink)"/>
  </svg>
  <h1 class="firm-name">Vale &amp; Brennick, Attorneys-at-Law, LLP</h1>
  <div class="address" style="top:18px">2140 E. Marlowe St.<br>Fort Worth, TX 76111</div>
  <div class="contacts" style="top:18px">
    <div><svg viewBox="0 0 10 10"><path d="M2 0.5 L3.6 2.4 L2.8 3.6 C3.4 5 4.8 6.4 6.4 7.2 L7.6 6.4 L9.5 8 L8.4 9.6 C4.6 9.4 0.6 5.4 0.4 1.6 Z" fill="var(--ink)"/></svg>(817) 555-0142</div>
    <div><svg viewBox="0 0 10 10"><rect x="2.5" y="0.5" width="5" height="3" fill="var(--ink)"/><rect x="0.5" y="3.5" width="9" height="4" rx="1" fill="var(--ink)"/><rect x="2.5" y="6.5" width="5" height="3" fill="var(--ink)"/></svg>(817) 555-0187</div>
  </div>
  <div class="letter-body">
    <p>Dear Addressee Name:</p>
    <p class="gap">Andipsum dipsum nostis nulpute magnissis niatie te molor adignis sequips uscipisit, sit vel ipsuscing ent lut lan ulla feugait augueraesto odolore doluptatio cons dolor sismodo luptatuero do od dolore magnim dolor auguero eu facilis ea core estrud eugiat velis ad tat dio odolor augue magna corting eugait enim venibh et, quatumsan hendre tincinisi tisisl dolute moloreet atem velesequat alit aliquat, vel dolore faciduis dolore dignis dolorper il eugiamconsed deliquamcon henis alis atum duis at.</p>
    <p>Bore del ute faccum vercill aorper sent alit, venis autet, quipsustio eugue vero dolore velendre euis nos nonse dolessim illa feum dolor sumsan ectet lortincin vulputat amet, qui esto conulput acil in eugait vel essequam zzriusto diam, velit wissit autat.</p>
    <p>Obore dolor incip ea conummy nulput vel ullan henisim am in ute erciliqui ex ent et, quis augiat, commod tis enis num delit laor acing elis dolorer se eugue feu facinci liquis aut lut nulluptat er sum zzrit vulla consequis accum incidunt iusci blaortio odoloreet pratum veliquatie modit, quat. Ut nummodo exercilisl iriliqu ipsusto dolesequat. Ut wisl in ute consequam ad diam vulputpat lan hent vel doloreet utat ver si.</p>
    <p class="gap">Vullaorem iusci blamcon seniamcommy nit iureetum dolore con ea faccum iureet prat. In utat acidunt nullum venismolum ing exer iusci bla augue magna consequi tem veliquis nostion utpat.</p>
    <p>Nibh euipis esed ero doluptat. Ibh ex exeros exero dolesed dunt pratissi euis nismodipsum eu feuguerit ipisl incilla faccum am init praese tat velis augue corem iriliqu amconsequat. Magnim ipit in ea acincil esto et wisl esenim volenit lorem del ut aut la commy nibh eui tiniam iure mod tem vel ipisit, quis nonsequi blan exerosto odolorem il irit num vel dolore et irit aute te dolestrud tin hent utet ut praestrud ea faccum venim venim il er iustion sequipsum quat.</p>
    <p class="gap">Do ea acilisis dolore min ercing endre consequat. Ero consequis ad euguerat, siscidunt laor sum iuscipis nullaoreet, velent ilit amconul laorperit lore diatum dui bla facipit irit alis ad dolorpe rostrud tem essequat praesequam, coreet ip er sim dit, velisim inciliquam, quis adigna feugue dolore et irillaor.</p>
    <p>Adiam zzrit,</p>
    <p class="signature">Veliquatin Veraessi</p>
  </div>
  <div class="partners" style="bottom:10px">Partners:<br><strong>Adrian Vale</strong>, Managing Partner (Licensed in State of Texas, United States District Court (Northern District of Texas), United States Supreme Court)<br><strong>Claire Marie Brennick</strong> (Licensed in the State of Texas)</div>
</section>

</body>
</html>
```